Financial investment calculator report for real estae - layout & design

I am looking to Create a web report utilizing the attached information. It is an investment calculator report that will be customized report based on an online calculator. Therefore the report will need to be designed in a manner that a backend developer will be able to build off of.

The report will need to be web based but also printed in PDF format. The report will need to include the calculation format as well as be templeted to add a report user unique profile information like Headshot, Business Logo, Name, Telephone number, email etc.

The report should be modern and clean and easy to read and use a modern clean template design. It should be able to be easily color customized by the end user to produce templets in Red, Blue, Green, and Greyscale.

The report should be no more than 3 pages total with out breaking up the sections.

Section One - Cover sheet including agent bio info, Report Title and property address (both prominent), 400 Character space for property description, Property Pictures (3), and a google Maps integration image showing property location, It should also have room for about 100 words for a text disclaimer. (I will provide text soon)

Section Two - Inputs from the calculator

Section 3 - The Four Benefits & Rates of Return

Once I have a completed/approved form I will have about a half dozen forms/reports that will need to be laid out with a similar aesthetic.

Feel free to ask me any questions. Thank You
Tobin
Updates

Target Market(s)

This report will be produced by real estate agents forvtheir investor clients. It should denote professionalism

Font styles to use
Sans Serif

Colors
0054AA
0677BA
7BADD7
CADEEF
E8F1F8
00AB8E
00BBA5
67D7C9
C6EFE9
E9F9F6
EB3D1F
EC4F4E
F09395
F8D3D4
FCEDEE

```html
<!DOCTYPE html>
<html lang="en">
<head>
<meta charset="utf-8">
<title>Investment Analysis Report – Cover Options</title>
<link href="https://fonts.googleapis.com/css2?family=Red+Hat+Display:wght@400;500;600;700&display=swap" rel="stylesheet">
<style>
  :root{
    --brand:#a51c24;
    --brand-soft:#f8d3d4;
    --ink:#2f2f33;
    --muted:#55565b;
    --panel:#e9e9ea;
    --card:#ebebec;
    --canvas:#f3f1f0;
    --page:#ffffff;
    --map:#eef0f2;
  }
  *{box-sizing:border-box;margin:0;padding:0}
  html,body{width:1200px;height:891px;overflow:hidden}
  body{background:var(--canvas);font-family:"Red Hat Display",Arial,sans-serif;color:var(--ink);position:relative}
  .page{position:absolute;top:131px;width:458px;height:592px;background:var(--page);border-radius:10px;overflow:hidden;box-shadow:0 2px 6px rgba(0,0,0,.12)}
  .page--one{left:129px}
  .page--two{left:613px}
  .abs{position:absolute}
  .meta{font-size:5px;top:6px}
  .header{left:0;top:0;width:100%}
  .header--brand{height:102px;background:var(--brand)}
  .header--neutral{height:100px;background:var(--panel)}
  .brandmark{display:flex;align-items:center;gap:6px}
  .brandmark__dot{width:34px;height:34px;border-radius:50%;border:2px solid currentColor}
  .brandmark__name{font-weight:600;letter-spacing:2px;line-height:1}
  .report-title{font-weight:600;font-size:22px;line-height:1.05;color:var(--ink)}
  .report-address{font-weight:700;font-size:21px;line-height:1.1;color:var(--brand)}
  .report-sub{font-size:10.5px;color:var(--brand)}
  .label{font-size:5.6px;letter-spacing:1.6px;font-weight:600;color:var(--muted)}
  .body-text{font-size:6.8px;line-height:1.45;color:#222}
  .photo{border-radius:6px}
  .photo--framed{border:2px solid #fff;box-shadow:0 0 0 1px #ddd}
  .map{background:var(--map);border-radius:6px;box-shadow:0 0 0 1px #e0e0e0}
  .agent-card{background:var(--card);border-radius:5px;text-align:center}
  .avatar{border-radius:50%;border:1.5px solid var(--brand);background:radial-gradient(circle at 50% 40%,#c9a58d,#5b6b82 70%)}
  .agent-line{font-size:8px;color:var(--muted);line-height:1.4}
  .agent-name{font-weight:600}
  .disclaimer-band{left:0;top:510px;width:100%;height:62px;background:var(--brand)}
  .footer{font-size:5px;color:#222}
  .option-label{font-size:6px;font-weight:700;top:797px}
</style>
</head>
<body>

<!-- Option 1 -->
<section class="page page--one">
  <div class="abs header header--brand"></div>
  <div class="abs meta" style="left:12px;color:#d7707a">5/30/23, 10:23 AM</div>
  <div class="abs meta" style="right:18px;color:#d7707a">Investment Analysis</div>
  <div class="abs brandmark" style="left:39px;top:35px;color:#fff">
    <span class="brandmark__dot"></span>
    <span class="brandmark__name" style="font-size:17px">MERIDIAN REALTY</span>
  </div>

  <div class="abs agent-card" style="left:303px;top:43px;width:117px;height:174px">
    <div class="abs avatar" role="img" aria-label="Agent headshot" style="left:22px;top:15px;width:72px;height:72px"></div>
    <div class="abs label" style="left:0;right:0;top:101px;color:var(--brand)">AGENT</div>
    <div class="abs agent-line" style="left:0;right:0;top:112px">
      <div class="agent-name">Greg Tobin</div>
      <div>admin1</div>
      <div>(555) 214-0198</div>
      <div>greg@meridianrealty.com</div>
    </div>
  </div>

  <div class="abs report-title" style="left:45px;top:129px">Investment Analysis</div>
  <div class="abs report-address" style="left:45px;top:153px">412 Larkspur</div>
  <div class="abs report-sub" style="left:45px;top:180px">15-Plex of 1bd/1bth Apartments</div>

  <div class="abs label" style="left:45px;top:219px">ABOUT THE PROPERTY</div>
  <p class="abs body-text" style="left:45px;top:230px;width:225px">Lorem ipsum is a placeholder text commonly used to demonstrate the visual form of a document or a typeface without relying on meaningful content.</p>

  <div class="abs photo photo--framed" role="img" aria-label="Exterior photo of the property at dusk" style="left:37px;top:283px;width:121px;height:108px;background:linear-gradient(#7d86b3,#c9a3b0 55%,#4a4f62)"></div>
  <div class="abs photo photo--framed" role="img" aria-label="Interior photo with blue wall and dresser" style="left:168px;top:283px;width:121px;height:108px;background:linear-gradient(#1e5a86,#204f75 60%,#6a4a34)"></div>
  <div class="abs photo photo--framed" role="img" aria-label="Living room photo with sofa and artwork" style="left:300px;top:283px;width:123px;height:108px;background:linear-gradient(#d9dedc,#c4cac8 60%,#8c9290)"></div>

  <div class="abs map" role="img" aria-label="Map showing the property location" style="left:37px;top:406px;width:386px;height:90px"></div>

  <div class="abs disclaimer-band"></div>
  <div class="abs label" style="left:42px;top:522px;color:var(--brand-soft)">DISCLAIMER</div>
  <p class="abs body-text" style="left:42px;top:536px;width:380px;color:var(--brand-soft)">In publishing and graphic design, Lorem ipsum is a placeholder text commonly used to demonstrate the visual form of a document or a typeface without relying on meaningful content. Lorem ipsum may be used as a placeholder before final copy is available.</p>

  <div class="abs footer" style="left:12px;top:582px">https://www.yieldreports.com/report/pdf/5</div>
  <div class="abs footer" style="right:18px;top:582px">1/3</div>
</section>

<!-- Option 2 -->
<section class="page page--two">
  <div class="abs header header--neutral"></div>
  <div class="abs meta" style="left:12px">5/30/23, 10:23 AM</div>
  <div class="abs meta" style="right:18px">Investment Analysis</div>
  <div class="abs brandmark" style="left:130px;top:33px;color:var(--brand)">
    <span class="brandmark__dot" style="width:40px;height:40px"></span>
    <span class="brandmark__name" style="font-size:17px">MERIDIAN REALTY</span>
  </div>

  <div class="abs report-title" style="left:0;right:0;top:134px;text-align:center">Investment Analysis</div>
  <div class="abs report-address" style="left:0;right:0;top:158px;text-align:center">412 Larkspur</div>
  <div class="abs report-sub" style="left:0;right:0;top:185px;text-align:center">15-Plex of 1bd/1bth Apartments</div>

  <div class="abs photo" role="img" aria-label="Exterior photo of the property at dusk" style="left:37px;top:228px;width:123px;height:97px;background:linear-gradient(#7d86b3,#c9a3b0 55%,#3f4558)"></div>
  <div class="abs photo" role="img" aria-label="Kitchen photo with island" style="left:167px;top:228px;width:123px;height:97px;background:linear-gradient(#e6e6e4,#bdbab5 60%,#6b5138)"></div>
  <div class="abs photo" role="img" aria-label="Bright kitchen photo" style="left:296px;top:228px;width:123px;height:97px;background:linear-gradient(#ebe7e0,#d2c8b9 60%,#a48d70)"></div>

  <div class="abs label" style="left:41px;top:356px">ABOUT THE PROPERTY</div>
  <p class="abs body-text" style="left:41px;top:369px;width:140px">Lorem ipsum is a placeholder text commonly used to demonstrate the visual form of a document or a typeface without relying on meaningful content.</p>
  <p class="abs body-text" style="left:41px;top:423px;width:140px">Lorem ipsum is a placeholder text commonly used to demonstrate the visual form of a document or a typeface</p>

  <div class="abs map" role="img" aria-label="Map showing the property location" style="left:223px;top:345px;width:194px;height:111px"></div>

  <div class="abs agent-card" style="left:56px;top:486px;width:150px;height:73px;text-align:left"></div>
  <div class="abs avatar" role="img" aria-label="Agent headshot" style="left:37px;top:496px;width:56px;height:56px"></div>
  <div class="abs agent-line" style="left:111px;top:501px">
    <div class="agent-name">Greg Tobin</div>
    <div>admin1</div>
    <div>(555) 214-0198</div>
    <div>greg@meridianrealty.com</div>
  </div>

  <div class="abs agent-card" style="left:213px;top:486px;width:204px;height:73px;text-align:left">
    <div class="abs" style="left:18px;top:15px;font-size:7px;font-weight:700;color:var(--muted)">DISCLAIMER</div>
    <p class="abs body-text" style="left:18px;top:25px;width:175px;color:var(--muted)">In publishing and graphic design, Lorem ipsum is a placeholder text commonly used to demonstrate the visual form of a document or a typeface</p>
  </div>

  <div class="abs footer" style="left:12px;top:582px">https://www.yieldreports.com/report/pdf/5</div>
  <div class="abs footer" style="right:18px;top:582px">1/3</div>
</section>

<div class="abs option-label" style="left:175px">OPTION 1</div>
<div class="abs option-label" style="left:626px">OPTION 2</div>

</body>
</html>
```